Plumber needs a business card

I need a new business card for my plumbing business. I dont have a logo at the moment but I want business cards that are simple but very professional. I want to look like
Name: Mitch Dorley
Address: (just make one up)
Phone: 0455 318 726
Email: mitch@dorleymail.com
Colors to use:
Blacks, blues, silvers

```html
<!DOCTYPE html>
<html lang="en">
<head>
<meta charset="utf-8">
<title>Mitch Dorley – Business Card</title>
<link href="https://fonts.googleapis.com/css2?family=Lato:wght@400;700&display=swap" rel="stylesheet">
<style>
  :root {
    --page-bg: #e6e9ee;
    --card-silver: #c9c9c9;
    --ink-black: #111111;
    --rule-black: #121212;
  }
  * { margin: 0; padding: 0; box-sizing: border-box; }
  html, body {
    width: 1200px;
    height: 665px;
    overflow: hidden;
    background: var(--page-bg);
    font-family: "Lato", sans-serif;
  }
  .business-card {
    position: absolute;
    left: 256px;
    top: 136px;
    width: 687px;
    height: 393px;
    border-radius: 18px;
    background: var(--card-silver);
    overflow: hidden;
    color: var(--ink-black);
    box-shadow: 0 6px 18px rgba(0,0,0,0.15);
  }
  .rule {
    position: absolute;
    background: var(--rule-black);
  }
  .rule--top-outer { left: 0; right: 0; top: 17px; height: 3px; }
  .rule--top-inner { left: 0; right: 0; top: 32px; height: 3px; }
  .rule--side-outer { top: 0; bottom: 0; left: 14px; width: 3px; }
  .rule--side-inner { top: 0; bottom: 0; left: 26px; width: 3px; }
  .holder-name {
    position: absolute;
    left: 69px;
    top: 57px;
    font-size: 24px;
    font-weight: 400;
    letter-spacing: 0.2px;
  }
  .address {
    position: absolute;
    right: 33px;
    top: 262px;
    font-size: 15px;
    line-height: 20px;
    text-align: left;
  }
  .contact-list {
    position: absolute;
    right: 26px;
    top: 337px;
    list-style: none;
    font-size: 15px;
    line-height: 20px;
  }
  .contact-item {
    display: flex;
    align-items: center;
    gap: 14px;
  }
  .contact-icon { width: 14px; height: 14px; flex: none; }
</style>
</head>
<body>
  <main class="business-card">
    <div class="rule rule--top-outer"></div>
    <div class="rule rule--top-inner"></div>
    <div class="rule rule--side-outer"></div>
    <div class="rule rule--side-inner"></div>

    <h1 class="holder-name">Mitch Dorley</h1>

    <address class="address" style="font-style: normal;">
      kestrel bend road<br>
      marlowe,northgate
    </address>

    <ul class="contact-list">
      <li class="contact-item">
        <svg class="contact-icon" viewBox="0 0 14 14" aria-hidden="true">
          <rect x="3.5" y="0.8" width="7" height="12.4" rx="1.2" fill="none" stroke="#111" stroke-width="1.4"/>
          <line x1="6" y1="11" x2="8" y2="11" stroke="#111" stroke-width="1.2"/>
        </svg>
        <span>0455 318 726</span>
      </li>
      <li class="contact-item">
        <svg class="contact-icon" viewBox="0 0 14 14" aria-hidden="true">
          <rect x="0.5" y="2.5" width="13" height="9.5" fill="#111"/>
          <polyline points="0.8,3 7,8 13.2,3" fill="none" stroke="#c9c9c9" stroke-width="1"/>
        </svg>
        <span>mitch@dorleymail.com</span>
      </li>
    </ul>
  </main>
</body>
</html>
```